cartNest - a stylish trolley for apartments

We neede a simple website to sell our Trolley, for apartment use.
The colour theme is red, blask & white. Our logo is attached and this needs to be on the Home page.
The website only needs a Home Page plus 4 other pges.
In the attachment you will find a site map.

You can check out the following two sites to see what I like:
www.plinthgallery.example/design-showcase-inspiration/minimalist-portfolio-website/
www.brightquarry.example/inspiration/40-beautiful-web-design-portfolios/ in this site especially
Dario Menezes
K B Forge
Nine 17 Studio
Oliver Marsh

And especially Lamp - I ike the simpicity of the site esp as we are only selling one product

Target Market(s)

Apartment dwellers

Industry/Entity Type

Apartment

Requirements
Must have
• This website must have 4 pages.
We need Corvo, Ledgerline and Quidly portals.
Order Form for Trolley
Payment form.

```html
<!DOCTYPE html>
<html lang="en">
<head>
<meta charset="utf-8">
<title>cartNest – a stylish trolley for apartments</title>
<link rel="stylesheet" href="https://fonts.googleapis.com/css2?family=Open+Sans:ital,wght@0,400;0,600;0,700;1,400&family=Tinos&display=swap">
<style>
:root{
  --red:#b8101a;
  --red-bright:#e8000f;
  --black:#000;
  --ink:#1a1a1a;
  --grey-text:#8a8a8a;
  --heading-grey:#555;
  --rule:#d4d4d4;
  --page:#efefef;
  --tab:#dedede;
  --link-blue:#1a6fc4;
  --white:#fff;
}
*{margin:0;padding:0;box-sizing:border-box}
html,body{width:1200px;height:1195px;overflow:hidden}
body{background:radial-gradient(ellipse at 50% 15%,#fafafa 0%,var(--page) 70%);font-family:"Open Sans",sans-serif;color:var(--ink);position:relative}
.abs{position:absolute}
.topbar{left:0;top:0;width:1200px;height:30px;background:var(--black);color:var(--white);font-size:12px}
.topbar .account-links{left:201px;top:7px}
.topbar .account-links span{margin:0 6px}
.currency-label{left:755px;top:7px;color:var(--red-bright);font-size:12px}
.currency-select{left:883px;top:4px;width:119px;height:21px;background:var(--white);color:#666;font-size:10px;padding:4px 6px}
.currency-select svg{position:absolute;right:6px;top:7px}
.brand{left:540px;top:58px;width:120px;text-align:center}
.brand-mark{width:22px;height:22px;background:var(--red);margin:0 auto 10px}
.brand-name{font-size:19px;font-weight:700;color:var(--red);}
.cart-status{left:890px;top:90px;font-size:13px;color:var(--red-bright)}
.cart-status small{color:#777;font-size:10px;margin-left:8px}
.follow{left:858px;top:121px;font-size:12px;color:#777;display:flex;align-items:center;gap:4px}
.follow i{display:inline-block;width:17px;height:17px;background:#666}
.rule{left:200px;width:803px;height:3px;background:var(--rule)}
.nav{left:200px;top:157px;width:803px;display:flex;justify-content:center;gap:31px}
.nav a{display:block;width:82px;height:24px;line-height:24px;text-align:center;font-size:12px;color:var(--ink);background:var(--tab);text-decoration:none}
.nav a.active{background:var(--red);color:var(--white)}
.banner{left:200px;top:210px;width:803px;height:262px;border:1px solid #ccc;background:linear-gradient(135deg,#8d8d8d,#5c5c5c 45%,#7a6a6a 60%,#8a8f98);padding:52px 28px}
.banner .photo{position:absolute;top:52px;width:229px;height:158px;border:1px solid #ddd}
.section-title{font-size:17px;color:var(--heading-grey)}
.section-title b{color:var(--red);font-weight:600}
.section-title strong{color:var(--ink);font-weight:600}
.about-title{left:212px;top:516px;display:flex;align-items:center;gap:10px}
.info-i{font-family:"Tinos",serif;font-style:italic;font-weight:700;color:var(--red);font-size:28px}
.lead{left:201px;top:567px;font-size:15px;font-style:italic}
.body-text{font-size:10.5px;color:var(--grey-text);line-height:19.5px}
.body-text a{color:var(--red);text-decoration:none}
.about-text{left:201px;top:593px;width:680px}
.feature{top:670px;width:230px}
.feature .photo{height:109px}
.feature h3{font-size:10px;font-style:italic;font-weight:400;margin:23px 0 10px}
.foot-title{top:928px}
.card-note{left:200px;top:977px;font-size:10px;font-style:italic}
.pay-box{left:200px;top:1017px;width:214px;height:68px;border:1px solid #aaa;background:var(--white)}
.pay-label{position:absolute;font-weight:700;font-size:15px;color:var(--ink)}
.contact{left:488px;top:975px;font-size:10px;font-style:italic;line-height:15px}
.contact p{margin-bottom:10px}
.contact a{color:var(--link-blue);text-decoration:none}
.map{left:774px;top:976px;width:192px;height:143px;background:linear-gradient(160deg,#e9e4da,#ddd7c8 60%,#cfd8e0)}
.footer{left:0;top:1167px;width:1200px;height:28px;background:var(--black);color:var(--white);font-family:"Tinos",serif;font-size:13px}
.footer nav{position:absolute;left:201px;top:7px;display:flex;gap:45px}
.footer nav .brand-word{color:var(--red-bright);font-family:"Open Sans",sans-serif;font-weight:700}
.footer .copy{position:absolute;right:197px;top:8px}
</style>
</head>
<body>
<header>
  <div class="abs topbar">
    <div class="abs account-links">My Account<span>|</span>My Cart<span>|</span>Checkout<span>|</span>Log In</div>
  </div>
  <div class="abs currency-label">Select Your Currency</div>
  <div class="abs currency-select">US Dollar - USD
    <svg width="9" height="6" viewBox="0 0 9 6"><path d="M0 0h9L4.5 6z" fill="#222"/></svg>
  </div>
  <div class="abs brand"><div class="brand-mark"></div><div class="brand-name">cartNest</div></div>
  <div class="abs cart-status">
    <svg width="22" height="18" viewBox="0 0 22 18" style="vertical-align:-3px;margin-right:6px"><path d="M1 2h4l3 10h10l2-7H7" fill="none" stroke="#333" stroke-width="1.6"/><circle cx="9" cy="15.5" r="1.6" fill="#333"/><circle cx="17" cy="15.5" r="1.6" fill="#333"/></svg>Cart: <small>(empty)</small>
  </div>
  <div class="abs follow">Follow us on :&nbsp;<i></i><i></i><i></i></div>
  <div class="abs rule" style="top:148px"></div>
  <nav class="abs nav">
    <a class="active" href="#">cartNest</a><a href="#">Gallery</a><a href="#">Contact Us</a><a href="#">Cart</a><a href="#">Payment</a>
  </nav>
  <div class="abs rule" style="top:186px"></div>
</header>

<main>
  <section class="abs banner">
    <div class="photo" role="img" aria-label="Trolley with red luggage in an apartment hallway" style="left:28px;background:linear-gradient(135deg,#b79a78,#6d5f55 50%,#9b3a34)"></div>
    <div class="photo" role="img" aria-label="Close-up of the chrome trolley frame" style="left:286px;background:linear-gradient(160deg,#c3ccd1,#a9b3ba 60%,#8b949b)"></div>
    <div class="photo" role="img" aria-label="Close-up of trolley wheels" style="left:543px;background:linear-gradient(180deg,#8e2a26,#3d3a38 45%,#cfc6bb)"></div>
  </section>

  <div class="abs about-title section-title"><span class="info-i">i</span><span>About <b>cartNest</b></span></div>
  <div class="abs rule" style="top:541px;height:2px"></div>
  <p class="abs lead">Lorem Ipsum is simply dummy text of the printing and typesetting industry.</p>
  <p class="abs body-text about-text">cartNest evolved from demand!&nbsp; Apartment dwellers everywhere are calling for a solution to moving shopping, luggage and other goods from car to apartment, and vice versa. Other trolleys on the market are not versatile, they are not robust, <a href="#">Read More ...</a></p>

  <article class="abs feature" style="left:201px">
    <div class="photo" role="img" aria-label="Man loading bags from a car onto the trolley" style="background:linear-gradient(135deg,#cfc36a,#7b7466 50%,#a9392f)"></div>
    <h3>Lorem Ipsum is simply dummy text.</h3>
    <p class="body-text">Lorem Ipsum has been the industry's stan-<br>dard dummy text ever since. <a href="#">Read More ...</a></p>
  </article>
  <article class="abs feature" style="left:487px">
    <div class="photo" role="img" aria-label="Two people beside a car and a loaded trolley in a car park" style="background:linear-gradient(135deg,#c9bf6a,#5e5a58 50%,#d2cfc8)"></div>
    <h3>Lorem Ipsum is simply dummy text.</h3>
    <p class="body-text">Lorem Ipsum has been the industry's stan-<br>dard dummy text ever since. <a href="#">Read More ...</a></p>
  </article>
  <article class="abs feature" style="left:774px">
    <div class="photo" role="img" aria-label="Woman unloading shopping from a car boot onto the trolley" style="background:linear-gradient(135deg,#cbc06c,#7e6b60 45%,#2f3a63)"></div>
    <h3>Lorem Ipsum is simply dummy text.</h3>
    <p class="body-text">Lorem Ipsum has been the industry's stan-<br>dard dummy text ever since. <a href="#">Read More ...</a></p>
  </article>

  <h2 class="abs section-title foot-title" style="left:200px">Pay by <b>Credit</b> <strong>or</strong> <b>Debit</b> <strong>Cards</strong></h2>
  <h2 class="abs section-title foot-title" style="left:488px">Contact <b>cartNest</b></h2>
  <h2 class="abs section-title foot-title" style="left:774px">Contact <b>Streetly</b> <strong>Map</strong></h2>
  <div class="abs rule" style="top:955px;height:2px"></div>

  <p class="abs card-note">We accept Corvo, Ledgerline and Quidly.</p>
  <div class="abs pay-box">
    <span class="pay-label" style="left:62px;top:-14px;background:var(--page);padding:0 4px">Quidly</span>
    <span class="pay-label" style="left:10px;top:28px">Corvo</span>
    <span class="pay-label" style="left:118px;top:28px">Ledgerline</span>
  </div>

  <div class="abs contact">
    <p>Lorem Ipsum is simply dummy text of the<br>printing and typesetting industry.</p>
    <p>E-mail : <a href="#">hello@cartnest.example</a></p>
    <p>Mobile : <a href="#">5550102030</a></p>
    <p>Tel no : <a href="#">5550102030</a></p>
  </div>
  <div class="abs map" role="img" aria-label="Street map showing the cartNest location"></div>
</main>

<footer class="abs footer">
  <nav><span class="brand-word">cartNest</span><span>Gallery</span><span>Contact Us</span><span>Cart</span><span>Payment</span></nav>
  <div class="copy">Copyright © All rights are reserved by Compny</div>
</footer>
</body>
</html>
```